Harbor SkyCare Global Air Ambulance Services
Harbor SkyCare Business Package
Harbor SkyCare Global Air Ambulance Services - Aerospace
Creative Brief
Professional
Mr. Doug Wilson Pratt
President / CEO
5273 West Dunmore Suite 410 Ridgeford, Arvale 85312-4706 United States of America
dpratt@harborskycare.example
http://www.harborskycare.example
jaxter42 jaxter42
Congratulations Morlund
vimal8marks vimal8marks
CH pls post feedback
HarborSkyCare HarborSkyCare
Looking away from any vertical formated cards
#191 - #194 - These pieces would be much more desirable if they were closer to our corporate colors: Again, please visit our website for reference: harborskycare.example
SiteAdmin SiteAdmin
Draft #160 by pario is a derivative of #119 by Tovesk, therefore has been taken down.
Draft #144 and its variation by bworkshopz are derivative of #119 by Tovesk, therefore have been taken down.
KDM27 KDM27
I was looking at your address and noticed I live about 5 minutes from there.... what a coincidence!
nanoGlyph nanoGlyph
please comment on my entry #129 and #131 thanks for your time nanoglyph
We love the punch out on #119
tinyrupa tinyrupa
wow alot of contestants, hehe.. i'm joining too in this project
minhcocoa minhcocoa
Thank you! Great comments!
First I want to begin by saying, “Thank you to everyone for participating”. Any ideas that we express are not meant to criticize or critique any designer(s). We simply want to allow you the ability to create “that piece that is just right” for our organization. 1.) I am not sure if maybe our in house design team has made the logo a little darker than the version I have uploaded: However, in order to get a good feeling of the corporate color, please visit our website; harborskycare.example: a. A good representation of what color we are looking for: #2 – The card in the upper right hand corner: On that card, we very much like the fade (bringing in more shadow towards the top ascending). b. Further, we also like the back of that card: 2.) The yellow / gold is too much & not what we are looking for: 3.) Many of the cards look like an “Insurance Identification Card”. 4.) #43 – We really like the drop shadow of the aircraft in the background: It also appears that there is a globe that is slightly visible – This looks very classy & exudes a first class service (This is image we are really trying to capture). 5.) #42 – We really like the shadow of the main portion of the logo 6.) #47 – The logo’s are all wrong: However, on what this person is portraying as the back of the card, the picture of the aircraft is sort of neat. The front of the card has WAY to much going on: 7.) We are most likely going to go with the rounded corners 8.) We are really liking the pictures on the card: Specifically, #57 & #58 captured our eye (with the picture positioning). 9.) We are looking for something that is very different from most business cards: We don’t want the same image for our organization 10.) Review our website for our companies colors: However, please don’t create anything that resembles “The sun burst” on the home page in the upper right hand corner (encompasses the words “Steady Wing Pledge”): We are not a fan of that any longer (I wasn’t a fan of that to begin with). I hope that some of this feedback will help everyone with a little better direction. Again, please understand that we are not trying to critique anyone (everyone has different tastes & we recognize that). Thank you for you for all of your efforts.

```html
<!DOCTYPE html>
<html lang="en">
<head>
<meta charset="utf-8">
<title>Harbor SkyCare Stationery Set</title>
<link rel="stylesheet" href="https://fonts.googleapis.com/css2?family=Roboto:wght@400;700&display=swap">
<style>
  :root {
    --backdrop: #6b6a63;
    --paper: #f3f1ec;
    --paper-shade: #dcd8cf;
    --brand: #9a1f66;
    --brand-deep: #6e1249;
    --brand-light: #c0478a;
    --accent: #e0562a;
    --ink: #55524c;
    --ink-soft: #8d8980;
    --white: #ffffff;
  }
  * { box-sizing: border-box; margin: 0; padding: 0; }
  html, body { width: 1200px; height: 720px; overflow: hidden; }
  body {
    background: var(--backdrop);
    font-family: "Roboto", Arial, sans-serif;
    position: relative;
  }
  .piece {
    position: absolute;
    background: linear-gradient(160deg, var(--paper) 40%, var(--paper-shade));
    box-shadow: 0 3px 8px rgba(0,0,0,.35);
    overflow: hidden;
  }
  .piece svg.wave { position: absolute; left: 0; bottom: 0; display: block; }
  .brand {
    position: absolute;
    display: flex;
    align-items: center;
    gap: 4px;
  }
  .brand-square { width: 9px; height: 9px; background: var(--accent); flex: none; }
  .brand-name { font-weight: 700; color: var(--brand); white-space: nowrap; }
  .brand-tagline {
    position: absolute;
    font-size: 4.5px;
    color: var(--ink-soft);
    letter-spacing: .3px;
    text-transform: uppercase;
    white-space: nowrap;
  }
  .faint-art {
    position: absolute;
    background: radial-gradient(ellipse at center, rgba(150,145,135,.18), rgba(150,145,135,0) 70%);
  }

  /* Letterhead */
  .letterhead { left: 185px; top: 115px; width: 355px; height: 504px; }
  .letterhead .brand { left: 22px; top: 24px; }
  .letterhead .brand-name { font-size: 13px; }
  .letterhead .brand-tagline { left: 35px; top: 41px; }
  .letterhead .faint-art { left: 110px; top: 200px; width: 190px; height: 200px; }
  .letterhead-footer {
    position: absolute; right: 14px; bottom: 10px;
    font-size: 5px; line-height: 7px; color: var(--white); text-align: right;
  }

  /* Envelope front */
  .envelope-front { left: 665px; top: 115px; width: 355px; height: 173px; }
  .envelope-front .brand { left: 18px; top: 18px; }
  .envelope-front .brand-name { font-size: 11px; }
  .envelope-front .brand-tagline { left: 30px; top: 33px; font-size: 4px; }
  .return-address {
    position: absolute; left: 140px; top: 18px;
    font-size: 4.5px; line-height: 6px; color: var(--ink-soft);
  }
  .address-window {
    position: absolute; left: 130px; top: 76px; width: 74px; height: 32px;
    background: var(--white); border-radius: 4px;
    box-shadow: inset 0 0 2px rgba(0,0,0,.15);
  }
  .envelope-front .faint-art { left: 150px; top: 20px; width: 150px; height: 120px; }

  /* Envelope back */
  .envelope-back { left: 665px; top: 331px; width: 355px; height: 168px; }
  .envelope-back svg.flap { position: absolute; left: 0; top: 0; }
  .envelope-back .brand { left: 50%; top: 16px; transform: translateX(-50%); }
  .envelope-back .brand-name { font-size: 7px; color: var(--white); }

  /* Business cards */
  .card { top: 548px; width: 160px; height: 72px; border-radius: 4px; }
  .card-front { left: 665px; }
  .card-back { left: 860px; }
  .card-front .brand { left: 7px; top: 6px; gap: 2px; }
  .card-front .brand-square { width: 5px; height: 5px; }
  .card-front .brand-name { font-size: 6px; }
  .portrait {
    position: absolute; left: 98px; top: 20px; width: 42px; height: 46px;
    background: linear-gradient(180deg, #b9b2a8, #4a4a4f);
  }
  .card-details {
    position: absolute; left: 8px; top: 18px; width: 60px;
    font-size: 2.8px; line-height: 3.8px; color: var(--ink);
  }
  .card-person {
    position: absolute; left: 98px; top: 6px; width: 58px;
    font-size: 2.6px; line-height: 3.4px; color: var(--ink);
  }
  .card-person strong { font-size: 3.2px; color: var(--brand); }
  .card-back .brand { left: 62px; top: 30px; gap: 3px; }
  .card-back .brand-square { width: 6px; height: 6px; }
  .card-back .brand-name { font-size: 8px; }
  .card-back-web {
    position: absolute; right: 10px; bottom: 6px;
    font-size: 3px; color: var(--white);
  }
</style>
</head>
<body>

<svg width="0" height="0" style="position:absolute">
  <defs>
    <linearGradient id="brandFade" x1="0" y1="0" x2="0" y2="1">
      <stop offset="0" stop-color="#5e0f3f"/>
      <stop offset=".45" stop-color="#9a1f66"/>
      <stop offset="1" stop-color="#b0387c"/>
    </linearGradient>
  </defs>
</svg>

<!-- Letterhead -->
<section class="piece letterhead">
  <div class="faint-art" role="img" aria-label="Faint aircraft shadow in the background"></div>
  <div class="brand"><span class="brand-square"></span><span class="brand-name">Harbor SkyCare</span></div>
  <div class="brand-tagline">Global Air Ambulance Services</div>
  <svg class="wave" width="355" height="80" viewBox="0 0 355 80">
    <path d="M0,62 C110,58 240,30 355,4 L355,80 L0,80 Z" fill="url(#brandFade)"/>
    <path d="M0,58 C110,54 240,26 355,0" fill="none" stroke="#c9c3b9" stroke-width="1"/>
  </svg>
  <div class="letterhead-footer">
    5273 West Dunmore Suite 410<br>
    Ridgeford, Arvale 85312-4706<br>
    United States of America<br>
    http://www.harborskycare.example
  </div>
</section>

<!-- Envelope front -->
<section class="piece envelope-front">
  <div class="faint-art" role="img" aria-label="Faint aircraft shadow in the background"></div>
  <div class="brand"><span class="brand-square"></span><span class="brand-name">Harbor SkyCare</span></div>
  <div class="brand-tagline">Global Air Ambulance Services</div>
  <div class="return-address">
    5273 West Dunmore Suite 410<br>
    Ridgeford, Arvale 85312-4706<br>
    United States of America<br>
    www.harborskycare.example
  </div>
  <div class="address-window"></div>
  <svg class="wave" width="355" height="58" viewBox="0 0 355 58">
    <path d="M0,34 C120,32 250,14 355,2 L355,58 L0,58 Z" fill="url(#brandFade)"/>
    <path d="M0,30 C120,28 250,10 355,-2" fill="none" stroke="#c9c3b9" stroke-width="1"/>
  </svg>
</section>

<!-- Envelope back -->
<section class="piece envelope-back">
  <svg class="flap" width="355" height="72" viewBox="0 0 355 72">
    <path d="M0,0 H355 V26 C280,30 215,40 177,70 C140,40 75,30 0,26 Z" fill="url(#brandFade)"/>
  </svg>
  <div class="brand"><span class="brand-name">Harbor SkyCare</span></div>
</section>

<!-- Business card front -->
<section class="piece card card-front">
  <div class="brand"><span class="brand-square"></span><span class="brand-name">Harbor SkyCare</span></div>
  <div class="card-details">
    5273 West Dunmore Suite 410<br>Ridgeford, Arvale 85312-4706<br>United States of America
  </div>
  <div class="portrait" role="img" aria-label="Portrait photo of the company president"></div>
  <div class="card-person">
    <strong>Mr. Doug Wilson Pratt</strong><br>
    President / CEO
  </div>
  <svg class="wave" width="160" height="16" viewBox="0 0 160 16">
    <path d="M0,12 C60,11 110,6 160,0 L160,16 L0,16 Z" fill="url(#brandFade)"/>
  </svg>
</section>

<!-- Business card back -->
<section class="piece card card-back">
  <div class="brand"><span class="brand-square"></span><span class="brand-name">Harbor SkyCare</span></div>
  <svg class="wave" width="160" height="22" viewBox="0 0 160 22">
    <path d="M0,18 C60,16 110,9 160,0 L160,22 L0,22 Z" fill="url(#brandFade)"/>
  </svg>
  <div class="card-back-web">www.harborskycare.example</div>
</section>

</body>
</html>
```